Business Card design for Property Developer

We need a business card design for a Melbourne based Property Developer called "Kestrelmoor Holdings Pty Ltd".

We subdivide land and onsell to builders etc.

We already have a company logo, which is attached. Also I have attached the layout requirements from the printer. We would like a 2-sided design with one side displaying our logo by itself and the other with the required info, such as name, address, tel no., email, abn etc. The card will need to be used by 4 members of staff so name and contact details should be interchangable.
Updates

If possible, can you please write "name' "job position" "phone" "email" "address" on the card but leave them so I can add the details at a later time. Thank you. Also I plan on printing with UV spot printing as a background on the card. Keep this is mind when designing.

Thanks again.

Hello designers, please do not include pics of houses, house plansĀ or construction machinery etc as we really do not like the way it looks. Thank you.

Target Market(s)

Real Estate Agents, Land Owners, Local Council Departments, Govt Bodies, other Developers etc.

Industry/Entity Type

Business

Requirements
Must have
• 2-sided design with one side displaying our logo by itself and the other with the required info, such as name, address, tel no., email, abn etc.

```html
<!DOCTYPE html>
<html lang="en">
<head>
<meta charset="utf-8">
<title>Kestrelmoor Holdings – Business Card</title>
<link rel="stylesheet" href="https://fonts.googleapis.com/css2?family=Open+Sans:ital,wdth,wght@0,75..100,300..800;1,75..100,300..800&display=swap">
<style>
  :root {
    --red-deep: #8e0f14;
    --red: #c8151d;
    --red-bright: #e0262a;
    --blue-deep: #1d2f8a;
    --blue: #2f57b0;
    --blue-light: #4a86c8;
    --cyan: #2bb3e6;
    --paper: #ecebe7;
    --paper-shade: #d9d8d3;
    --white: #ffffff;
    --label-red: #e0393b;
    --canvas: #ffffff;
  }
  * { margin: 0; padding: 0; box-sizing: border-box; }
  html, body {
    width: 1200px; height: 900px; overflow: hidden;
    background: var(--canvas);
    font-family: "Open Sans", Arial, sans-serif;
  }
  .card {
    position: absolute; top: 296px;
    width: 512px; height: 320px; overflow: hidden;
    box-shadow: 0 2px 6px rgba(0,0,0,0.25);
  }
  .card--front { left: 63px; }
  .card--back { left: 635px; }
  .card__art { position: absolute; inset: 0; width: 100%; height: 100%; }

  .brand {
    position: absolute; left: 0; right: 0; top: 92px;
    display: flex; flex-direction: column; align-items: center;
  }
  .brand__mark {
    width: 78px; height: 78px; border-radius: 50%;
    background: var(--blue);
    margin-bottom: 14px;
  }
  .brand__name {
    color: var(--red);
    font-weight: 800; font-stretch: 85%;
    font-size: 32px; line-height: 1.0; letter-spacing: 0.5px;
    text-transform: uppercase; text-align: center;
  }

  .contact { position: absolute; left: 38px; color: var(--white); }
  .contact__name {
    top: 20px; font-size: 20px; font-weight: 800; font-stretch: 80%;
    letter-spacing: 0.3px; text-transform: uppercase;
  }
  .contact__role {
    top: 46px; font-size: 15px; font-weight: 700; font-style: italic;
    letter-spacing: 1.5px;
  }
  .contact__lines { top: 88px; font-size: 12.5px; line-height: 19px; }
  .contact__label { color: var(--label-red); margin-right: 6px; }
  .contact__address { top: 200px; font-size: 12.5px; line-height: 19px; }
  .contact__web { top: 252px; font-size: 12.5px; line-height: 19px; }
  .contact__abn { color: var(--cyan); }
</style>
</head>
<body>

<section class="card card--front" aria-label="Card front">
  <svg class="card__art" viewBox="0 0 512 320" aria-hidden="true">
    <defs>
      <linearGradient id="front-red" x1="0" y1="0" x2="0" y2="1">
        <stop offset="0" stop-color="#b3151b"/>
        <stop offset="1" stop-color="#7d0c10"/>
      </linearGradient>
      <linearGradient id="front-paper" x1="0" y1="0" x2="0" y2="1">
        <stop offset="0" stop-color="#f1f0ec"/>
        <stop offset="1" stop-color="#dcdbd6"/>
      </linearGradient>
    </defs>
    <rect width="512" height="320" fill="url(#front-red)"/>
    <path d="M0,150 H72 C90,150 94,128 102,112 A175,150 0 0 1 410,112 C418,128 422,150 440,150 H512 V320 H0 Z"
          fill="var(--blue)"/>
    <path d="M0,160 H78 C96,160 100,138 110,120 A168,142 0 0 1 402,120 C412,138 416,160 434,160 H512 V320 H0 Z"
          fill="url(#front-paper)"/>
  </svg>
  <div class="brand">
    <div class="brand__mark"></div>
    <p class="brand__name">Kestrelmoor<br>Holdings</p>
  </div>
</section>

<section class="card card--back" aria-label="Card back">
  <svg class="card__art" viewBox="0 0 512 320" aria-hidden="true">
    <defs>
      <radialGradient id="back-red" cx="0.35" cy="0.6" r="0.8">
        <stop offset="0" stop-color="#e0262a"/>
        <stop offset="1" stop-color="#8e0f14"/>
      </radialGradient>
      <linearGradient id="back-blue" x1="0" y1="0" x2="0" y2="1">
        <stop offset="0" stop-color="#4a86c8"/>
        <stop offset="1" stop-color="#1d2f8a"/>
      </linearGradient>
      <radialGradient id="back-disc" cx="0.45" cy="0.45" r="0.6">
        <stop offset="0" stop-color="#f1f0ec"/>
        <stop offset="1" stop-color="#d9d8d3"/>
      </radialGradient>
    </defs>
    <rect width="512" height="152" fill="url(#back-red)"/>
    <rect y="152" width="512" height="168" fill="url(#back-blue)"/>
    <rect y="148" width="512" height="6" fill="var(--blue)"/>
    <circle cx="410" cy="155" r="140" fill="url(#back-disc)"/>
  </svg>

  <p class="contact contact__name">Firstname Lastname</p>
  <p class="contact contact__role">Position Title</p>
  <p class="contact contact__lines">
    <span class="contact__label">[T]</span>0400 000 000<br>
    <span class="contact__label">[E]</span>Name@KestrelmoorHoldings.com
  </p>
  <p class="contact contact__address">
    Street Address Line 1<br>
    City, Australia, Postal Code
  </p>
  <p class="contact contact__web">
    www.KestrelmoorHoldings.com<br>
    <span class="contact__abn">ABN: 11 101 101 101</span>
  </p>
</section>

</body>
</html>
```